Simple, Professional and neat business card design for Vendralo Inc.

We're looking to re-vamp our business card design. We're a supplier of innovative feed ingredients for the North American animal agriculture industry. We are located in Lucknow, Ontario, Canada and our flagship product is a product that prevents milk fever in dairy cows when the calve, it is fed before calving and is very effective compared to other alternatives available on the market today.

Our company has Danish roots and we import all of our product from our Danish partner/manufacturer in Denmark. We like our design to embrace high professionalism while remaining neat and simple.

Target Market(s)

B2B, Feed Mills, Veterinary Clinics, Large integrators/producers,

Industry/Entity Type

Agribusiness

Contact Information for Business Card

We like the rounded corners because they make the card easy to sit in a wallet and not many use it so it makes the card stand out, just possibly something to take account for during the design.

As you can also see on the sliders below, looking for a that simple but proffesional scandinavian design.

Requirements
Nice to have
• Rounded corners
Should not have
• Too vibrant

```html
<!DOCTYPE html>
<html lang="en">
<head>
<meta charset="utf-8">
<title>Vendralo Inc. Business Card</title>
<link href="https://fonts.googleapis.com/css2?family=Montserrat:wght@400;500;700;800&display=swap" rel="stylesheet">
<style>
  :root {
    --brand-blue: #0f4fa0;
    --brand-blue-deep: #0a3577;
    --brand-blue-light: #1a67bd;
    --ink: #3a3a3c;
    --ink-soft: #555558;
    --paper: #f3f3f2;
    --rule: #b9b9bb;
    --backdrop: #d9dbde;
    --reverse-text: #e4e8ee;
  }
  * { box-sizing: border-box; margin: 0; padding: 0; }
  html, body {
    width: 1200px; height: 900px; overflow: hidden;
    background: var(--backdrop);
    font-family: "Montserrat", sans-serif;
  }
  .sheet {
    width: 1200px; height: 900px;
    display: flex; flex-direction: column;
    align-items: center; justify-content: center; gap: 44px;
  }
  .card {
    width: 600px; height: 343px;
    border-radius: 38px;
    position: relative; overflow: hidden;
    box-shadow: 0 10px 28px rgba(0,0,0,0.18);
  }

  /* Front */
  .card-front { background: var(--paper); display: flex; }
  .front-brand {
    width: 300px; padding-left: 40px; padding-right: 16px;
    display: flex; flex-direction: column; justify-content: center;
  }
  .brand-mark {
    width: 34px; height: 34px; background: var(--brand-blue);
    margin-left: 150px; margin-bottom: 10px;
  }
  .brand-name {
    font-weight: 800; font-size: 25px; letter-spacing: -0.3px;
    color: var(--brand-blue); text-transform: uppercase;
    white-space: nowrap;
  }
  .brand-web {
    margin-top: 12px; font-size: 14px; color: var(--ink-soft);
  }
  .brand-web strong { color: var(--brand-blue); font-weight: 700; }
  .front-divider {
    width: 1px; background: var(--rule);
    margin: 64px 0;
  }
  .front-contact {
    flex: 1; padding: 0 24px 0 30px;
    display: flex; flex-direction: column; justify-content: center;
    color: var(--ink);
  }
  .contact-name {
    font-weight: 800; font-size: 21px; color: var(--brand-blue);
    white-space: nowrap;
  }
  .contact-email { font-size: 13.5px; color: var(--ink-soft); margin-top: 2px; }
  .contact-address { font-size: 13.5px; margin-top: 14px; line-height: 1.45; }
  .contact-phones { list-style: none; margin-top: 10px; font-size: 13.5px; line-height: 1.5; }
  .contact-phones b { font-weight: 700; }

  /* Back */
  .card-back {
    background: linear-gradient(160deg, var(--brand-blue-light) 0%, var(--brand-blue) 45%, var(--brand-blue-deep) 100%);
    display: flex; flex-direction: column; align-items: center; justify-content: center;
  }
  .back-mark {
    width: 40px; height: 40px; background: var(--reverse-text); margin-bottom: 22px;
  }
  .back-name {
    font-weight: 800; font-size: 44px; letter-spacing: -0.5px;
    color: var(--reverse-text); text-transform: uppercase;
    white-space: nowrap;
  }
  .back-tagline {
    margin-top: 12px; font-size: 17px; font-weight: 500;
    color: var(--reverse-text); letter-spacing: 0.5px;
  }
</style>
</head>
<body>
<main class="sheet">
  <section class="card card-front">
    <div class="front-brand">
      <span class="brand-mark"></span>
      <p class="brand-name">Vendralo Inc.</p>
      <p class="brand-web">www.<strong>vendralo</strong>.com</p>
    </div>
    <div class="front-divider"></div>
    <div class="front-contact">
      <h1 class="contact-name">Mikkel Sørensen</h1>
      <p class="contact-email">mikkel@vendralo.com</p>
      <p class="contact-address">Box 427, Harlow Creek<br>Ontario, Canada K9X 4K7</p>
      <ul class="contact-phones">
        <li><b>Mobile</b> - 555.555.0147</li>
        <li><b>Office</b> - 555.555.0192</li>
        <li><b>Fax</b> - 555.555.0168</li>
        <li><b>Toll Free</b> - 888.555.0126</li>
      </ul>
    </div>
  </section>

  <section class="card card-back">
    <span class="back-mark"></span>
    <p class="back-name">Vendralo Inc.</p>
    <p class="back-tagline">Caring For The Wellbeing Of Your Herds</p>
  </section>
</main>
</body>
</html>
```